Oregon Pawnbroker About Us Brochure

We need to make a front/back tri-fold "about us" informative brochure using the bullet points uploaded. Our association represents licensed pawnbrokers in the state of Oregon and this will be distributed to the entire legislative body in our state. I have attached our logo, but feel free to be creative with logo to enhance the overall appearance of the brochure.

Target Market(s)

Regulators and Politicians

Industry/Entity Type

Pawnbroker

Requirements
Must have
• Professional Appearance
Nice to have
• Graphics, color scheme

```html
<!DOCTYPE html>
<html lang="en">
<head>
<meta charset="utf-8">
<title>Oregon Pawn Lenders Guild – About Us Brochure</title>
<link href="https://fonts.googleapis.com/css2?family=Libre+Baskerville:ital,wght@0,400;1,400&family=Lato:wght@400;700;900&display=swap" rel="stylesheet">
<style>
:root{
  --backdrop:#2b2b2b;
  --paper:#ffffff;
  --panel-grey:#d3d3d3;
  --panel-grey-light:#e4e4e4;
  --ink:#1d1d1d;
  --ink-soft:#333333;
  --orange:#f26a21;
  --orange-deep:#ee5a1a;
  --yellow:#f8b817;
  --navy:#0f1b2b;
  --stat-grey:#ececec;
}
*{box-sizing:border-box;margin:0;padding:0}
html,body{width:1047px;height:1200px;overflow:hidden;background:var(--backdrop)}
.stage{position:absolute;left:0;top:0;width:1100px;height:1261px;transform:scale(0.95182);transform-origin:0 0;font-family:'Lato',sans-serif;color:var(--ink)}
.spread{position:absolute;left:202px;width:728px;background:var(--paper);overflow:hidden}
.spread--outside{top:44px;height:562px}
.spread--inside{top:648px;height:560px}
.spread svg.art{position:absolute;left:0;top:0}
.abs{position:absolute}
.serif{font-family:'Libre Baskerville',serif;font-weight:400}
.heading{text-align:center;line-height:1.05;color:var(--ink)}
.accent{color:var(--orange)}
.bullets{list-style:none;font-size:9.6px;line-height:1.27;color:var(--ink-soft)}
.bullets li{position:relative;padding-left:8px;margin-bottom:7px}
.bullets li::before{content:"";position:absolute;left:0;top:4px;width:3.5px;height:3.5px;border-radius:50%;background:var(--orange)}
.stat{position:absolute;width:99px;height:97px;display:flex;flex-direction:column;align-items:center;justify-content:center;text-align:center;font-size:9.6px;line-height:1.3;padding:4px}
.stat--grey{background:var(--stat-grey);border:1px solid #c9c9c9}
.stat--yellow{background:var(--yellow);color:#fff}
.stat--orange{background:var(--orange);color:#fff}
.stat--outline{background:var(--stat-grey);border:1px solid var(--yellow)}
.stat strong{font-weight:900}
.stat .big{font-size:15px;font-weight:900;margin-top:8px}
.emph{color:var(--orange);font-weight:900;font-size:12px}
.badge{position:absolute;border-radius:50%;background:#fff;box-shadow:0 2px 8px rgba(0,0,0,.25);border:4px solid #f0f0f0;display:flex;align-items:center;justify-content:center;text-align:center}
.badge span{font-family:'Lato',sans-serif;font-weight:900;font-size:10.5px;line-height:1.2;color:var(--ink);letter-spacing:.5px}
.url-pill{position:absolute;left:488px;top:516px;width:226px;height:28px;border-radius:14px;background:var(--navy);color:#fff;font-size:10.6px;display:flex;align-items:center;justify-content:center}
.pill-heading{position:absolute;left:511px;top:30px;width:188px;height:28px;border-radius:14px;background:linear-gradient(90deg,var(--orange),var(--yellow));color:#fff;font-family:'Libre Baskerville',serif;font-size:16px;display:flex;align-items:center;justify-content:center;letter-spacing:.5px}
.regulators{list-style:none;font-size:9.6px;font-weight:700;line-height:1.25;color:var(--ink)}
.regulators li{position:relative;padding-left:7px}
.regulators li::before{content:"";position:absolute;left:0;top:4px;width:3px;height:3px;border-radius:50%;background:var(--orange)}
.rule{position:absolute;height:1px;background:var(--yellow)}
</style>
</head>
<body>
<div class="stage">

  <!-- Outside spread -->
  <section class="spread spread--outside">
    <svg class="art" width="728" height="562" viewBox="0 0 728 562">
      <defs>
        <linearGradient id="band" x1="0" x2="1"><stop offset="0" stop-color="#ee5a1a"/><stop offset="1" stop-color="#f8c21a"/></linearGradient>
        <linearGradient id="greyPhoto" x1="0" y1="0" x2="0" y2="1"><stop offset="0" stop-color="#c4c4c4"/><stop offset="1" stop-color="#d6d6d6"/></linearGradient>
        <linearGradient id="coverFade" x1="0" y1="0" x2="0" y2="1"><stop offset="0" stop-color="#ffffff"/><stop offset="1" stop-color="#dcdcdc"/></linearGradient>
        <linearGradient id="moneyPhoto" x1="0" y1="0" x2="1" y2="1"><stop offset="0" stop-color="#2a3550"/><stop offset=".55" stop-color="#6b4a33"/><stop offset="1" stop-color="#8a6446"/></linearGradient>
        <linearGradient id="deskPhoto" x1="0" y1="0" x2="1" y2="1"><stop offset="0" stop-color="#eeeeee"/><stop offset="1" stop-color="#cfd2d6"/></linearGradient>
      </defs>
      <rect x="241" y="0" width="242" height="562" fill="var(--panel-grey)"/>
      <rect x="483" y="0" width="245" height="562" fill="url(#coverFade)"/>
      <rect x="241" y="11" width="242" height="240" fill="url(#greyPhoto)" role="img" aria-label="Faded photo of shelved ledgers"/>
      <path d="M380,11 L728,11 L728,250 Q640,292 520,262 Q395,225 380,11 Z" fill="url(#moneyPhoto)" role="img" aria-label="Photo of cash being handed across a wooden desk"/>
      <path d="M483,275 Q620,300 728,248" fill="none" stroke="var(--yellow)" stroke-width="7"/>
      <path d="M0,385 Q120,350 241,420 L241,562 L0,562 Z" fill="url(#deskPhoto)" role="img" aria-label="Photo of a laptop showing charts on a desk"/>
      <path d="M0,385 Q120,350 241,420" fill="none" stroke="var(--orange)" stroke-width="7"/>
      <rect x="0" y="0" width="728" height="11" fill="url(#band)"/>
      <circle cx="606" cy="507" r="10" fill="var(--orange)"/>
      <circle cx="606" cy="507" r="5" fill="none" stroke="var(--navy)" stroke-width="1.4"/>
      <line x1="601" y1="507" x2="611" y2="507" stroke="var(--navy)" stroke-width="1"/>
    </svg>

    <div class="abs heading serif" style="left:0;top:42px;width:241px;font-size:15px">OREGON<br>PAWNBROKER<br><span class="accent">STATISTICS</span></div>
    <div class="abs serif" style="left:0;top:99px;width:241px;text-align:center;font-size:10px;font-style:italic">(as reported by DCBS)</div>

    <div class="stat stat--grey" style="left:18px;top:135px">Oregon pawnshops made approximately <span class="emph">206,500 loans</span> in 2020, lending <span><span class="emph">$33.2 million</span> to</span> Oregon customers.</div>
    <div class="stat stat--yellow" style="left:126px;top:135px">Average loan amount in 2020 was<span class="big">$175</span></div>
    <div class="stat stat--orange" style="left:18px;top:242px">Police pickup rate of<span class="big">0.085%</span></div>
    <div class="stat stat--outline" style="left:126px;top:242px">2015 through 2020 Average Rate of Redemption<span class="big" style="color:var(--orange);font-size:12px">73.5%</span></div>

    <div class="abs heading serif" style="left:241px;top:279px;width:242px;font-size:16px">WHY PAWNBROKERS<br>ARE <span class="accent">IMPORTANT</span> TO<br>OREGON CONSUMERS</div>
    <ul class="bullets abs" style="left:254px;top:352px;width:216px">
      <li>Without state-licensed pawnbrokers, Oregonians could be forced to borrow from unlicensed people with unregulated loans that include very high interest rates or instead, forced to sell their property entirely, diminishing their personal assets.</li>
      <li>Other credit based lenders, such as banks and credit unions, do not offer Oregonians loan products at the small dollar amounts our industry serves.</li>
      <li>Pawnbrokers provide a same day financial solution.</li>
      <li>Pawnbrokers are invested in our communities and are sensitive to the needs of our customers.</li>
    </ul>

    <div class="badge" style="left:539px;top:230px;width:144px;height:144px"><span>OREGON<br>PAWN LENDERS<br>GUILD</span></div>
    <div class="abs heading serif" style="left:483px;top:394px;width:245px;font-size:25px;line-height:1.07">OREGON<br>PAWN LENDERS<br>GUILD</div>
    <div class="url-pill">www.oregonpawnlendersguild.org</div>
  </section>

  <!-- Inside spread -->
  <section class="spread spread--inside">
    <svg class="art" width="728" height="560" viewBox="0 0 728 560">
      <defs>
        <linearGradient id="bandIn" x1="0" x2="1"><stop offset="0" stop-color="#ee5a1a"/><stop offset="1" stop-color="#f8c21a"/></linearGradient>
        <linearGradient id="handPhoto" x1="0" y1="0" x2="1" y2="0"><stop offset="0" stop-color="#a9b4bd"/><stop offset=".5" stop-color="#8e8c86"/><stop offset="1" stop-color="#c9c2b4"/></linearGradient>
        <radialGradient id="scalesPhoto"><stop offset="0" stop-color="#c79a5c"/><stop offset=".7" stop-color="#8a6f55"/><stop offset="1" stop-color="#d9dde2"/></radialGradient>
      </defs>
      <rect x="245" y="0" width="242" height="560" fill="var(--panel-grey)"/>
      <path d="M0,11 L370,11 L370,110 Q330,205 200,215 Q80,222 0,180 Z" fill="url(#handPhoto)" role="img" aria-label="Photo of two people shaking hands"/>
      <path d="M0,185 Q90,232 210,222 Q330,210 372,120" fill="none" stroke="var(--orange)" stroke-width="7"/>
      <circle cx="606" cy="437" r="100" fill="url(#scalesPhoto)" stroke="var(--yellow)" stroke-width="2.5" role="img" aria-label="Photo of brass scales of justice"/>
      <rect x="0" y="0" width="728" height="11" fill="url(#bandIn)"/>
      <rect x="0" y="549" width="728" height="11" fill="url(#bandIn)"/>
    </svg>

    <div class="badge" style="left:295px;top:28px;width:144px;height:144px"><span>OREGON<br>PAWN LENDERS<br>GUILD</span></div>

    <div class="abs serif accent" style="left:0;top:272px;width:245px;text-align:center;font-size:16px">About the</div>
    <div class="abs heading serif" style="left:0;top:304px;width:245px;font-size:22px;line-height:1.08">OREGON<br>PAWN LENDERS<br>GUILD</div>
    <div class="rule" style="left:40px;top:379px;width:166px"></div>
    <ul class="bullets abs" style="left:28px;top:408px;width:200px;font-size:10.4px">
      <li style="margin-bottom:12px">United voice of Oregon Pawnbrokers</li>
      <li style="margin-bottom:12px">Represents majority of pawnbrokers, both by numbers of licensees and transactions processed</li>
      <li>Single point of contact for Oregon Legislature and all regulators to communicate with our industry.</li>
    </ul>

    <div class="abs heading serif" style="left:245px;top:216px;width:242px;font-size:17px">ABOUT<br>OUR INDUSTRY</div>
    <ul class="bullets abs" style="left:257px;top:276px;width:220px">
      <li>Pawnbroking is the oldest form of regulated consumer credit.</li>
      <li>The Department of Consumer and Business Services issues the pawnbroker licenses here in Oregon.</li>
      <li>Currently, Oregon has <b>83</b> individually licensed pawnshops, <b>78</b> of which are brick-and-mortar, family-owned and operated businesses.</li>
      <li>Pawnbrokers offer highly regulated safety-net funds to consumers on a face-to-face basis from Main Street locations across the state.</li>
      <li>Lending decisions are solely based on the collateral and pawn transactions are non-recourse. No credit inquiries, No credit reporting, No collections, No cycle of debt.</li>
      <li>Pawnbrokers provide safe, secure storage for items customers cannot or do not want to store themselves, including oversized or seasonal items, construction equipment, and firearms.</li>
    </ul>

    <div class="pill-heading">REGULATION</div>
    <ul class="bullets abs" style="left:493px;top:86px;width:220px">
      <li>Pawnshops are heavily regulated and work closely with the federal, state and local governments and law enforcement.</li>
      <li>ORS 726 and OAR 441-740 define the requirements for our industry here in Oregon including the requirements of a loan, duration of a loan, as well as the interest &amp; fees charged.</li>
      <li>Transactions require customer to present government issued photo identification.</li>
      <li>All transactions are reported daily to law enforcement.</li>
      <li>Oregon Pawnbrokers work closely with the following regulators:</li>
    </ul>
    <ul class="regulators abs" style="left:503px;top:270px;width:220px">
      <li>Department of Consumer &amp; Business Services</li>
      <li>Bureau of Alcohol Tobacco and Firearms</li>
      <li>State Police</li>
      <li>Department of Agriculture</li>
    </ul>
  </section>

</div>
</body>
</html>
```